Veltarum

Standard Business Card design.
Sample two-sided design uploaded. White front, Black back.
Would like white shield to be on all black background side.
Willing to look at a couple creative designs, but nothing crazy.
Preference for a classic, confident, strong design.

```html
<!DOCTYPE html>
<html lang="en">
<head>
<meta charset="utf-8">
<title>Veltarum — Business Card</title>
<link href="https://fonts.googleapis.com/css2?family=Montserrat:wght@400;500;700&display=swap" rel="stylesheet">
<style>
  :root {
    --backdrop: #3a3a3a;
    --card-white: #ffffff;
    --card-black: #111111;
    --ink: #151515;
    --ink-soft: #2a2a2a;
    --paper-text: #f4f4f4;
    --rule: #9a9a9a;
  }
  * { margin: 0; padding: 0; box-sizing: border-box; }
  html, body {
    width: 1200px; height: 1200px; overflow: hidden;
    background: var(--backdrop);
    font-family: "Montserrat", sans-serif;
  }
  .sheet {
    width: 1200px; height: 1200px;
    display: flex; flex-direction: column; align-items: center; justify-content: center;
    gap: 60px;
  }
  .card {
    width: 700px; height: 400px;
    border-radius: 36px;
    position: relative;
    overflow: hidden;
    box-shadow: 0 18px 40px rgba(0,0,0,0.45);
  }
  .card-front { background: var(--card-white); color: var(--ink); }
  .card-back  { background: var(--card-black); color: var(--paper-text); }

  .front-brand {
    position: absolute; top: 70px; right: 70px;
    display: flex; align-items: center; gap: 14px;
  }
  .brand-square { width: 26px; height: 26px; background: currentColor; }
  .brand-name {
    font-weight: 700; font-size: 34px; letter-spacing: 3px; text-transform: uppercase;
  }

  .contact-block { position: absolute; left: 70px; bottom: 52px; }
  .person-name { font-weight: 700; font-size: 36px; letter-spacing: 1px; line-height: 1; }
  .person-title { font-weight: 400; font-size: 18px; letter-spacing: 1px; margin: 6px 0 16px 18px; }
  .contact-list { list-style: none; margin-left: 18px; }
  .contact-list li {
    display: flex; align-items: flex-start; gap: 12px;
    font-size: 17px; line-height: 1.3; color: var(--ink-soft);
  }
  .contact-list svg { width: 18px; height: 18px; flex: none; margin-top: 2px; fill: var(--ink); }

  .back-brand {
    position: absolute; inset: 0;
    display: flex; align-items: center; justify-content: center; gap: 20px;
  }
  .back-brand .brand-name { font-size: 54px; letter-spacing: 6px; }
  .back-brand .brand-square { width: 40px; height: 40px; }
</style>
</head>
<body>
<main class="sheet">
  <section class="card card-front" aria-label="Card front">
    <div class="front-brand">
      <span class="brand-square"></span>
      <span class="brand-name">Veltarum</span>
    </div>
    <div class="contact-block">
      <h1 class="person-name">FULL NAME</h1>
      <p class="person-title">TITLE</p>
      <ul class="contact-list">
        <li><svg viewBox="0 0 24 24"><path d="M6.6 10.8a15 15 0 0 0 6.6 6.6l2.2-2.2a1 1 0 0 1 1-.25 11.4 11.4 0 0 0 3.6.57 1 1 0 0 1 1 1V20a1 1 0 0 1-1 1A17 17 0 0 1 3 4a1 1 0 0 1 1-1h3.5a1 1 0 0 1 1 1c0 1.25.2 2.45.57 3.57a1 1 0 0 1-.25 1z"/></svg>(000) 000 0000</li>
        <li><svg viewBox="0 0 24 24"><path d="M2 5h20v14H2z M4 7l8 6 8-6" fill="none" stroke="#151515" stroke-width="2"/></svg>email@veltarum.com</li>
        <li><svg viewBox="0 0 24 24"><g fill="none" stroke="#151515" stroke-width="1.8"><circle cx="12" cy="12" r="9.5"/><ellipse cx="12" cy="12" rx="4.5" ry="9.5"/><path d="M2.5 12h19M4 7h16M4 17h16"/></g></svg>www.veltarum.com</li>
        <li><svg viewBox="0 0 24 24"><path d="M12 2a7 7 0 0 0-7 7c0 5 7 13 7 13s7-8 7-13a7 7 0 0 0-7-7zm0 9.5A2.5 2.5 0 1 1 12 6.5a2.5 2.5 0 0 1 0 5z"/></svg><span>123 Name Street, 000<br>Your City, 00000-000</span></li>
      </ul>
    </div>
  </section>

  <section class="card card-back" aria-label="Card back">
    <div class="back-brand">
      <span class="brand-square"></span>
      <span class="brand-name">Veltarum</span>
    </div>
  </section>
</main>
</body>
</html>
```